Vorlix is about building a community in the events space.

Looking to build Gadgetriver.com style website, with the following key features / functionality:
• Sign up / sign in page
• Profile pages - User / Speaker / Event Organiser
• Event categories and listings
• Ratings / Review Comments

Preferably for Wordpress platform, as in Wordpress plugin, with PHP access.

Target Market(s)

Event communities

Industry/Entity Type

Building

Coding

Coded - Design and coding required

Number of Pages Required

5+ page

Font styles to use
Sans Serif

Colors
0492cd

Requirements
Must have
• Vorlix is about building a community in the events space.
• Looking to build Gadgetriver.com style website, with the following key features / functionality:
• • Sign up / sign in page
• • Profile pages - User / Speaker / Event Organiser
• • Event categories and listings
• • Ratings / Review Comments
• Preferably for Wordpress platform, as in Wordpress plugin, with PHP access.

```html
<!DOCTYPE html>
<html lang="en">
<head>
<meta charset="utf-8">
<title>Vorlix – Profile</title>
<link href="https://fonts.googleapis.com/css2?family=Montserrat:wght@400;500;600;700&display=swap" rel="stylesheet">
<style>
:root{
  --blue:#0492cd;
  --blue-light:#2aa8f2;
  --blue-top:#1b9df0;
  --ink:#333;
  --muted:#777;
  --line:#dcdcdc;
  --panel:#f7f7f7;
  --green:#7ab51d;
  --white:#fff;
}
*{box-sizing:border-box;margin:0;padding:0}
html,body{width:1190px;height:1200px;overflow:hidden;background:var(--white);font-family:"Montserrat",sans-serif;color:var(--ink)}
.page{position:relative;width:1190px;height:1200px}
.abs{position:absolute}

/* header */
.topbar{left:0;top:0;width:1190px;height:100px;background:linear-gradient(90deg,var(--blue-top),var(--blue-light))}
.brand{left:122px;top:30px;color:var(--white);font-size:34px;font-weight:600;letter-spacing:1px}
.search{left:265px;top:35px;width:343px;height:29px;border:2px solid rgba(255,255,255,.75);display:flex;align-items:center;color:var(--white);font-size:13px}
.search svg{margin:0 10px 0 14px}
.search span{border-left:1px solid rgba(255,255,255,.7);padding-left:10px;height:19px;line-height:19px}
.menu-dots{left:715px;top:36px;width:46px;height:29px;border:2px solid var(--white);color:var(--white);font-size:10px;text-align:center;line-height:24px;letter-spacing:3px}
.divider-v{left:771px;top:41px;width:1px;height:18px;background:rgba(255,255,255,.7)}
.login{left:792px;top:42px;color:var(--white);font-size:13px}
.signup{left:846px;top:36px;width:71px;height:29px;border:2px solid var(--white);color:var(--white);font-size:13px;text-align:center;line-height:25px}
.social-ring{top:33px;width:34px;height:34px;border:2px solid rgba(255,255,255,.7);border-radius:50%}

/* profile */
.avatar{left:98px;top:118px;width:213px;height:213px;border-radius:50%;background:radial-gradient(circle at 50% 45%,#c98a6c,#8a5a40 55%,#c7c7c7 80%)}
.name{left:326px;top:140px;font-size:27px;font-weight:500;color:#444}
.handle{left:329px;top:171px;font-size:14px;color:#666}
.bio{left:328px;top:192px;width:488px;font-size:15.5px;line-height:20px;color:#555;text-align:justify}
.stat{top:264px;width:74px;height:65px;background:#efefef;text-align:center}
.stat b{display:block;font-size:31px;font-weight:700;color:#333;margin-top:6px;line-height:34px}
.stat small{font-size:11px;font-weight:600;color:#333}
.follow{left:489px;top:265px;width:80px;height:64px;background:linear-gradient(180deg,#3ab4f6,var(--blue-top));color:var(--white);font-size:12px;font-weight:700;text-align:center;line-height:64px;letter-spacing:.5px}
.about-title{left:100px;top:350px;font-size:26px;font-weight:500;color:#444}
.about-text{left:99px;top:393px;width:184px;font-size:11.5px;line-height:20.4px;color:#666;text-align:justify;letter-spacing:.2px}

/* events */
.events{left:326px;top:356px;width:533px;height:654px;border:1px solid var(--line)}
.tabs{height:44px;border-bottom:1px solid var(--line);position:relative;background:var(--white)}
.filter{position:absolute;left:16px;top:10px;width:73px;height:26px;background:var(--blue-top);color:var(--white);font-size:12px;display:flex;align-items:center;gap:8px;padding-left:10px}
.tab-list{position:absolute;right:16px;top:12px;display:flex;align-items:center;font-size:12.5px;color:#444}
.tab-list .on{background:var(--blue-top);color:var(--white);font-weight:600;padding:2px 10px}
.tab-list .sep{margin:0 14px;color:#555}
.event{height:152.5px;border-bottom:1px solid var(--line);background:var(--panel);position:relative}
.event:last-child{border-bottom:none}
.event .thumb{position:absolute;left:15px;top:22px;width:135px;height:102px}
.event .title{position:absolute;left:171px;top:22px;display:flex;align-items:center;gap:10px;font-size:21px;color:#444}
.event .place{position:absolute;right:14px;top:28px;border:1px solid #8bc9f0;font-size:10.5px;color:#555;padding:2px 6px}
.event .desc{position:absolute;left:171px;top:57px;font-size:11.5px;color:#666}
.event .votes{position:absolute;left:172px;top:103px;border:1px solid #555;font-size:12px;color:#444;padding:1px 5px;background:var(--white)}
.event .meta{position:absolute;right:14px;top:104px;display:flex;align-items:center;gap:4px;font-size:11.5px;color:#777}

/* sidebar */
.share{left:880px;top:132px;width:132px;height:26px;background:var(--green);color:var(--white);font-size:11.5px;display:flex;align-items:center;gap:7px;padding-left:12px}
.share-sq{top:132px;width:28px;height:26px;background:var(--blue-top)}
.card{left:878px;width:215px;border:1px solid #e3e3e3;background:var(--white)}
.card h3{height:35px;background:var(--blue-top);color:var(--white);font-size:14.5px;font-weight:500;line-height:37px;padding-left:13px;letter-spacing:.3px}
.speaker{display:flex;align-items:center;height:65px;margin:0 11px;border-bottom:1px solid #e3e3e3;position:relative}
.speaker .pic{width:42px;height:42px;border-radius:50%;background:radial-gradient(circle,#b07b5d,#5b3a2a);margin-left:2px}
.speaker .info{margin-left:9px}
.speaker .info b{display:block;font-size:11px;font-weight:600;color:#333;margin-bottom:6px}
.speaker .info span{font-size:9.5px;color:#888}
.speaker svg{position:absolute;right:0;top:25px}
.more{font-size:11px;color:#222;padding:14px 12px 13px}
.comment{margin:0 11px;padding:17px 9px 12px;border-bottom:1px solid #e3e3e3;font-size:11px;line-height:13px;color:#222;text-align:justify}
.comment p{margin-bottom:10px}
.comment .by{padding-left:2px}
.topics{list-style:none;padding:18px 0 12px 12px}
.topics li{font-size:10.5px;color:#333;height:32.5px;display:flex;gap:10px}

/* footer */
.band{left:96px;top:1073px;width:996px;height:60px;background:repeating-linear-gradient(135deg,#ececec 0 1px,#f8f8f8 1px 4px)}
.band-brand{left:110px;top:1093px;font-size:18px;color:#222}
.foot-circle{top:1087px;width:34px;height:34px;border-radius:50%;background:var(--blue-top)}
.love{left:612px;top:1092px;font-size:17px;font-weight:500;color:#222}
.email{left:834px;top:1088px;width:153px;height:31px;border:1px solid #bbb;background:var(--white);font-size:11px;color:#777;display:flex;align-items:center;justify-content:space-between;padding:0 12px}
.join{left:987px;top:1088px;width:71px;height:31px;background:var(--blue-top);color:var(--white);font-size:12px;font-weight:700;text-align:center;line-height:31px}
.foot-links{left:113px;top:1150px;font-size:11.5px;color:#222;display:flex;gap:18px}
.copy{left:732px;top:1157px;font-size:11px;color:#222}
.mark{left:1120px;top:1157px;font-size:11px;color:#222}
</style>
</head>
<body>
<div class="page">

  <header class="abs topbar"></header>
  <div class="abs brand">Vorlix</div>
  <div class="abs search">
    <svg width="13" height="13" viewBox="0 0 14 14"><circle cx="6" cy="6" r="4.5" fill="none" stroke="#fff" stroke-width="2"/><path d="M9.5 9.5L13 13" stroke="#fff" stroke-width="2"/></svg>
    <span>Discover your next favorite event...</span>
  </div>
  <div class="abs menu-dots">○○○</div>
  <div class="abs divider-v"></div>
  <div class="abs login">Login</div>
  <div class="abs signup">Sign Up</div>
  <div class="abs social-ring" style="left:945px" aria-label="Social link"></div>
  <div class="abs social-ring" style="left:988px" aria-label="Social link"></div>
  <div class="abs social-ring" style="left:1031px" aria-label="Social link"></div>

  <div class="abs avatar" role="img" aria-label="Profile photo of Jennifer"></div>
  <h1 class="abs name">Jennifer</h1>
  <div class="abs handle">@jennifer</div>
  <p class="abs bio">Neque porro quisquam est qui dolorem ipsum quia dolor sit amet, consectetur, adipisci velit...</p>
  <div class="abs stat" style="left:325px"><b>217</b><small>Followers</small></div>
  <div class="abs stat" style="left:407px"><b>98</b><small>Following</small></div>
  <div class="abs follow">FOLLOW</div>

  <h2 class="abs about-title">About Me</h2>
  <p class="abs about-text">Sed ut perspiciatis unde omnis iste natus error sit voluptatem accusantium doloremque laudantium, totam rem aperiam, eaque ipsa quae ab illo inventore veritatis et quasi architecto beatae vitae dicta sunt explicabo. Nemo enim ipsam voluptatem quia voluptas sit aspernatur aut odit aut fugit,</p>

  <section class="abs events">
    <div class="tabs">
      <div class="filter">
        <svg width="18" height="16" viewBox="0 0 18 16" fill="none" stroke="#fff" stroke-width="1.4"><path d="M3 1v14M9 1v14M15 1v14"/><rect x="1" y="9" width="4" height="3" fill="#1b9df0"/><rect x="7" y="3" width="4" height="3" fill="#1b9df0"/><rect x="13" y="8" width="4" height="3" fill="#1b9df0"/></svg>
        Filter
      </div>
      <div class="tab-list"><span class="on">Upvoted</span><span class="sep">|</span>Attended<span class="sep">|</span>Spoken</div>
    </div>

    <div class="event">
      <div class="thumb" role="img" aria-label="Concert crowd under stage lights" style="background:radial-gradient(circle at 55% 30%,#f6b07a,#c3392a 45%,#2a0f0c 90%)"></div>
      <div class="title"><svg width="12" height="16" viewBox="0 0 12 16"><path d="M1.5 1.5h9v13l-4.5-3.5-4.5 3.5z" fill="none" stroke="#1b9df0" stroke-width="1.6"/></svg>Event Name</div>
      <div class="place">Sydney,Australia</div>
      <div class="desc">Lorem ipsum dolor sit amet, consectetur adipiscing elit....</div>
      <div class="votes">▲534</div>
      <div class="meta"><svg width="76" height="12" viewBox="0 0 76 12"><g fill="#1b9df0"><path id="s" d="M6 0.5l1.6 3.7 4 .3-3 2.6 1 3.9L6 9 2.4 11l1-3.9-3-2.6 4-.3z"/><use href="#s" x="16"/><use href="#s" x="32"/><use href="#s" x="48"/></g><path d="M70 0.5l1.6 3.7 4 .3-3 2.6 1 3.9L70 9l-3.6 2 1-3.9-3-2.6 4-.3z" fill="none" stroke="#1b9df0"/></svg>&nbsp;(133)&nbsp;&nbsp;<svg width="13" height="11" viewBox="0 0 13 11"><path d="M6.5 1C3.5 1 1 2.7 1 4.8c0 1.1.7 2.1 1.8 2.8L2 10l3-1.4c.5.1 1 .1 1.5.1 3 0 5.5-1.7 5.5-3.9S9.5 1 6.5 1z" fill="none" stroke="#1b9df0"/></svg>(26)</div>
    </div>

    <div class="event">
      <div class="thumb" role="img" aria-label="Speaker at a laptop facing an audience" style="background:linear-gradient(110deg,#1d3a6b 35%,#c4533a 60%,#e6a57a)"></div>
      <div class="title"><svg width="12" height="16" viewBox="0 0 12 16"><path d="M1.5 1.5h9v13l-4.5-3.5-4.5 3.5z" fill="none" stroke="#1b9df0" stroke-width="1.6"/></svg>Event Name</div>
      <div class="place">Sydney,Australia</div>
      <div class="desc">Lorem ipsum dolor sit amet, consectetur adipiscing elit....</div>
      <div class="votes">▲534</div>
      <div class="meta"><svg width="76" height="12" viewBox="0 0 76 12"><g fill="#1b9df0"><use href="#s"/><use href="#s" x="16"/><use href="#s" x="32"/><use href="#s" x="48"/></g><path d="M70 0.5l1.6 3.7 4 .3-3 2.6 1 3.9L70 9l-3.6 2 1-3.9-3-2.6 4-.3z" fill="none" stroke="#1b9df0"/></svg>&nbsp;(133)&nbsp;&nbsp;<svg width="13" height="11" viewBox="0 0 13 11"><path d="M6.5 1C3.5 1 1 2.7 1 4.8c0 1.1.7 2.1 1.8 2.8L2 10l3-1.4c.5.1 1 .1 1.5.1 3 0 5.5-1.7 5.5-3.9S9.5 1 6.5 1z" fill="none" stroke="#1b9df0"/></svg>(26)</div>
    </div>

    <div class="event">
      <div class="thumb" role="img" aria-label="Business people reviewing documents" style="background:linear-gradient(120deg,#c9d3dc,#3a4250 50%,#d8c3b0)"></div>
      <div class="title"><svg width="12" height="16" viewBox="0 0 12 16"><path d="M1.5 1.5h9v13l-4.5-3.5-4.5 3.5z" fill="none" stroke="#1b9df0" stroke-width="1.6"/></svg>Event Name</div>
      <div class="place">Sydney,Australia</div>
      <div class="desc">Lorem ipsum dolor sit amet, consectetur adipiscing elit....</div>
      <div class="votes">▲534</div>
      <div class="meta"><svg width="76" height="12" viewBox="0 0 76 12"><g fill="#1b9df0"><use href="#s"/><use href="#s" x="16"/><use href="#s" x="32"/><use href="#s" x="48"/></g><path d="M70 0.5l1.6 3.7 4 .3-3 2.6 1 3.9L70 9l-3.6 2 1-3.9-3-2.6 4-.3z" fill="none" stroke="#1b9df0"/></svg>&nbsp;(133)&nbsp;&nbsp;<svg width="13" height="11" viewBox="0 0 13 11"><path d="M6.5 1C3.5 1 1 2.7 1 4.8c0 1.1.7 2.1 1.8 2.8L2 10l3-1.4c.5.1 1 .1 1.5.1 3 0 5.5-1.7 5.5-3.9S9.5 1 6.5 1z" fill="none" stroke="#1b9df0"/></svg>(26)</div>
    </div>

    <div class="event">
      <div class="thumb" role="img" aria-label="Banquet hall lit in purple" style="background:radial-gradient(circle at 50% 60%,#e4b7f0,#8a3ab0 50%,#2b0f3a)"></div>
      <div class="title"><svg width="12" height="16" viewBox="0 0 12 16"><path d="M1.5 1.5h9v13l-4.5-3.5-4.5 3.5z" fill="none" stroke="#1b9df0" stroke-width="1.6"/></svg>Event Name</div>
      <div class="place">Sydney,Australia</div>
      <div class="desc">Lorem ipsum dolor sit amet, consectetur adipiscing elit....</div>
      <div class="votes">▲534</div>
      <div class="meta"><svg width="76" height="12" viewBox="0 0 76 12"><g fill="#1b9df0"><use href="#s"/><use href="#s" x="16"/><use href="#s" x="32"/><use href="#s" x="48"/></g><path d="M70 0.5l1.6 3.7 4 .3-3 2.6 1 3.9L70 9l-3.6 2 1-3.9-3-2.6 4-.3z" fill="none" stroke="#1b9df0"/></svg>&nbsp;(133)&nbsp;&nbsp;<svg width="13" height="11" viewBox="0 0 13 11"><path d="M6.5 1C3.5 1 1 2.7 1 4.8c0 1.1.7 2.1 1.8 2.8L2 10l3-1.4c.5.1 1 .1 1.5.1 3 0 5.5-1.7 5.5-3.9S9.5 1 6.5 1z" fill="none" stroke="#1b9df0"/></svg>(26)</div>
    </div>
  </section>

  <div class="abs share">
    <svg width="11" height="11" viewBox="0 0 12 12" fill="#fff"><circle cx="9.5" cy="2.5" r="2"/><circle cx="2.5" cy="6" r="2"/><circle cx="9.5" cy="9.5" r="2"/><path d="M2.5 6l7-3.5M2.5 6l7 3.5" stroke="#fff" stroke-width="1.2"/></svg>
    Share this Profile
  </div>
  <div class="abs share-sq" style="left:1019px" aria-label="Share link"></div>
  <div class="abs share-sq" style="left:1053px" aria-label="Share link"></div>

  <aside class="abs card" style="top:174px">
    <h3>TRENDING SPEAKERS</h3>
    <div class="speaker"><div class="pic" role="img" aria-label="Speaker photo"></div><div class="info"><b>Tara Welles</b><span>Reviews 2 , Followers 5</span></div><svg width="15" height="12" viewBox="0 0 15 12" fill="#999"><circle cx="5" cy="3" r="2.8"/><path d="M0 11c0-3 2.2-4.5 5-4.5s5 1.5 5 4.5z"/><path d="M12 3v5M9.5 5.5h5" stroke="#999" stroke-width="1.5"/></svg></div>
    <div class="speaker"><div class="pic" role="img" aria-label="Speaker photo"></div><div class="info"><b>Tara Welles</b><span>Reviews 2 , Followers 5</span></div><svg width="15" height="12" viewBox="0 0 15 12" fill="#999"><circle cx="5" cy="3" r="2.8"/><path d="M0 11c0-3 2.2-4.5 5-4.5s5 1.5 5 4.5z"/><path d="M12 3v5M9.5 5.5h5" stroke="#999" stroke-width="1.5"/></svg></div>
    <div class="speaker"><div class="pic" role="img" aria-label="Speaker photo"></div><div class="info"><b>Tara Welles</b><span>Reviews 2 , Followers 5</span></div><svg width="15" height="12" viewBox="0 0 15 12" fill="#999"><circle cx="5" cy="3" r="2.8"/><path d="M0 11c0-3 2.2-4.5 5-4.5s5 1.5 5 4.5z"/><path d="M12 3v5M9.5 5.5h5" stroke="#999" stroke-width="1.5"/></svg></div>
    <div class="speaker"><div class="pic" role="img" aria-label="Speaker photo"></div><div class="info"><b>Tara Welles</b><span>Reviews 2 , Followers 5</span></div><svg width="15" height="12" viewBox="0 0 15 12" fill="#999"><circle cx="5" cy="3" r="2.8"/><path d="M0 11c0-3 2.2-4.5 5-4.5s5 1.5 5 4.5z"/><path d="M12 3v5M9.5 5.5h5" stroke="#999" stroke-width="1.5"/></svg></div>
    <div class="more">Read More</div>
  </aside>

  <aside class="abs card" style="top:523px">
    <h3>RECENT COMMENTS</h3>
    <div class="comment"><p>Lorem ipsum dolor sit amet, consectetur adipiscing elit, sed do eiusmod tempor incididunt ut labore et...</p><div class="by">By - Linda</div></div>
    <div class="comment"><p>Lorem ipsum dolor sit amet, consectetur adipiscing elit, sed do eiusmod tempor incididunt ut labore et...</p><div class="by">By - Jhon</div></div>
    <div class="more">Read More</div>
  </aside>

  <aside class="abs card" style="top:820px">
    <h3>FOLLOWED TOPICS</h3>
    <ul class="topics">
      <li><span>›</span>Finibus Bonorum et Malorum</li>
      <li><span>›</span>Nostrum exercitationem</li>
      <li><span>›</span>Duis aute irure dolor</li>
      <li><span>›</span>Nor again is there anyone</li>
      <li><span>›</span>Finibus Bonorum et Malorum</li>
    </ul>
  </aside>

  <footer>
    <div class="abs band"></div>
    <div class="abs band-brand">@we are Vorlix</div>
    <div class="abs foot-circle" style="left:258px" aria-label="Social link"></div>
    <div class="abs foot-circle" style="left:302px" aria-label="Social link"></div>
    <div class="abs foot-circle" style="left:345px" aria-label="Social link"></div>
    <div class="abs love">Do you Love our Events?</div>
    <div class="abs email">Enter Email id<svg width="11" height="9" viewBox="0 0 11 9"><rect x=".5" y=".5" width="10" height="8" fill="none" stroke="#777"/><path d="M.5 .5l5 4 5-4" fill="none" stroke="#777"/></svg></div>
    <div class="abs join">Join Now</div>
    <nav class="abs foot-links"><span>About Us</span><span>:</span><span>Contact Us</span><span>:</span><span>Team</span><span>:</span><span>Careers</span></nav>
    <div class="abs copy">Copyrights © 2017, www.companyname.com. All Rights Reserved.</div>
    <div class="abs mark">M1</div>
  </footer>

</div>
</body>
</html>
```